Menu Design Project for an Italian cafe

Casual Italian style cafe situated in Chinatown in Sydney Australia . Value for money food, good coffee and good location are the cafes strengths. Catering to bushiness crowd in the morning/lunch, tourist crowd for brunch and Asian customers for late afternoon coffee.
Design concept is understated, casual European chic. Should communicate a casual escape to have a good meet up with friends to escape the hustle and bustle of the city crowd.
Would like to move away from current colors of dark brown, creme, black and orange. Would like a more enticing vibrant and brighter colour scheme.

```html
<!DOCTYPE html>
<html lang="en">
<head>
<meta charset="utf-8">
<title>Caffè Lumi – Menus</title>
<link rel="stylesheet" href="https://fonts.googleapis.com/css2?family=Bebas+Neue&family=Oswald:wght@500&family=Libre+Baskerville&display=swap">
<style>
:root{
  --bg:#efece6;
  --paper:#ffffff;
  --ink:#3a3a3a;
  --ink-soft:#6b6b6b;
  --coral:#d9574f;
  --rule:#f0b3ad;
  --board:#3b3b3b;
  --khaki:#cfcdb0;
  --ring:#9a9a9a;
  --photo-a:#b3322a;
  --photo-b:#6a4a33;
}
*{box-sizing:border-box;margin:0;padding:0}
html,body{width:1200px;height:900px;overflow:hidden;background:var(--bg)}
body{position:relative;font-family:"Libre Baskerville",serif;color:var(--ink)}

.menu{position:absolute;top:130px;width:410px;height:640px;background:var(--paper);
  box-shadow:0 4px 14px rgba(0,0,0,.18);padding:26px 28px;text-align:center}
.menu--breakfast{left:40px}
.menu--dinner{left:470px}

.brand{display:flex;align-items:center;justify-content:center;gap:7px;
  font-family:"Oswald",sans-serif;font-weight:500;font-size:17px;color:var(--coral);letter-spacing:1px}
.brand__dot{width:16px;height:16px;border-radius:50%;background:var(--coral)}

.menu__title{font-family:"Bebas Neue",sans-serif;font-weight:400;font-size:30px;letter-spacing:4px;margin-top:16px;text-transform:uppercase}
.divider{font-size:11px;color:var(--ink-soft);letter-spacing:2px;margin:4px 0 10px}
.rule{height:2px;background:var(--rule);opacity:.6;margin:0 -10px}

.section-title{font-family:"Bebas Neue",sans-serif;font-weight:400;font-size:21px;letter-spacing:4px;color:var(--ink-soft);
  text-transform:uppercase;margin:10px 0 10px}

.item{margin-bottom:8px}
.item__name{font-family:"Oswald",sans-serif;font-weight:500;font-size:10px;text-transform:uppercase;letter-spacing:.3px}
.item__desc{font-size:7px;color:var(--ink-soft);margin-top:1px}

.special{position:relative;background:var(--board);color:#fff;margin:14px 30px 14px 2px;padding:8px 12px;
  clip-path:polygon(10px 0,calc(100% - 10px) 0,100% 10px,100% calc(100% - 10px),calc(100% - 10px) 100%,10px 100%,0 calc(100% - 10px),0 10px)}
.special::after{content:"";position:absolute;inset:3px;border:1px solid rgba(255,255,255,.7)}
.special__title{font-family:"Bebas Neue",sans-serif;font-size:18px;letter-spacing:2px;text-transform:uppercase}
.special__text{font-size:8px;line-height:1.4;margin-top:3px}

.mains{margin-top:8px}
.mains__list{position:relative;padding-top:14px}
.mains__list::before{content:"";position:absolute;left:10px;right:10px;top:0;height:22px;
  border:1px solid var(--rule);border-bottom:none}
.mains__list::after{content:"";position:absolute;left:24px;right:24px;top:6px;height:16px;
  border:1px solid var(--rule);border-bottom:none}

.plates{display:grid;grid-template-columns:1fr 1fr;column-gap:16px;row-gap:6px;margin:6px 0 10px}
.plates .item{margin:0}

.card{position:absolute;left:910px;top:230px;width:250px;height:390px;background:var(--paper);
  border-radius:14px;box-shadow:0 4px 14px rgba(0,0,0,.2);overflow:hidden}
.card__binding{height:40px;background:var(--khaki);display:flex;justify-content:center;gap:30px;padding-top:6px}
.card__ring{width:10px;height:30px;border:3px solid var(--ring);border-radius:6px;background:var(--paper)}
.card__body{position:relative;height:350px}
.card__photo{position:absolute;inset:0;background:radial-gradient(ellipse at 45% 60%,var(--photo-a),var(--photo-b) 75%)}
.card__title{position:relative;font-family:"Bebas Neue",sans-serif;font-weight:400;font-size:22px;color:#fff;letter-spacing:3px;
  text-transform:uppercase;text-align:center;padding-top:14px}
.card__text{position:relative;font-size:9px;line-height:1.4;color:#fff;text-align:center;padding:6px 22px}
</style>
</head>
<body>

<article class="menu menu--breakfast">
  <div class="brand"><span class="brand__dot"></span>Caffè Lumi</div>
  <h1 class="menu__title">Breakfast Menu</h1>
  <div class="divider">···//···</div>
  <div class="rule"></div>
  <h2 class="section-title">Starters &amp; Salads</h2>
  <div class="item"><div class="item__name">Crostinis, Pastas, Cold Starters</div><div class="item__desc">walnuts, cheese, walnuts, cheese, walnuts, cheese, w/ walnuts, cheese &amp; walnuts, cheese</div></div>
  <div class="item"><div class="item__name">Country Style Spreads</div><div class="item__desc">walnuts, cheese, walnuts, cheese, walnuts, cheese, w/ walnuts, cheese &amp; walnuts, cheese</div></div>
  <div class="special">
    <div class="special__title">Special</div>
    <p class="special__text">eiusmod tempor incididunt ut labore et dolore magna aliqua.<br>Ut enim ad minim veniam, culpa qui officia deserunt mollit anim id est laborum</p>
  </div>
  <div class="rule"></div>
  <section class="mains">
    <h2 class="section-title">Main Courses</h2>
    <div class="mains__list">
      <div class="item"><div class="item__name">Country Style Spreads</div><div class="item__desc">walnuts, cheese, walnuts, cheese, walnuts, cheese, w/ walnuts, cheese &amp; walnuts, cheese</div></div>
      <div class="item"><div class="item__name">Country Style Spreads</div><div class="item__desc">walnuts, cheese, walnuts, cheese, walnuts, cheese, w/ walnuts, cheese &amp; walnuts, cheese</div></div>
      <div class="item"><div class="item__name">Traditional Style Soups for Vegetarians</div><div class="item__desc">walnuts, cheese, walnuts, cheese, walnuts, cheese, w/ walnuts, cheese &amp; walnuts, cheese</div></div>
      <div class="item"><div class="item__name">Country Spreads</div><div class="item__desc">walnuts, cheese, walnuts, cheese, walnuts, cheese, w/ walnuts, cheese &amp; walnuts, cheese</div></div>
    </div>
  </section>
</article>

<article class="menu menu--dinner">
  <div class="brand"><span class="brand__dot"></span>Caffè Lumi</div>
  <h1 class="menu__title">Dinner Menu</h1>
  <div class="divider">···//···</div>
  <div class="rule"></div>
  <h2 class="section-title">Starters &amp; Salads</h2>
  <div class="item"><div class="item__name">Crostinis, Pastas, Cold Starters</div><div class="item__desc">walnuts, cheese, walnuts, cheese, walnuts, cheese, w/ walnuts, cheese &amp; walnuts, cheese</div></div>
  <div class="item"><div class="item__name">Country Style Spreads</div><div class="item__desc">walnuts, cheese, walnuts, cheese, walnuts, cheese, w/ walnuts, cheese &amp; walnuts, cheese</div></div>
  <div class="plates">
    <div class="item"><div class="item__name">Antipasto Duo</div><div class="item__desc">picante bread, chilli, meat &amp; armadillo</div></div>
    <div class="item"><div class="item__name">Picante Plate</div><div class="item__desc">picante bread, chilli, meat &amp; armadillo</div></div>
    <div class="item"><div class="item__name">Rustic Plate</div><div class="item__desc">picante bread, chilli, meat &amp; armadillo</div></div>
    <div class="item"><div class="item__name">Picante Plate and Taco</div><div class="item__desc">picante bread, chilli, meat &amp; armadillo</div></div>
    <div class="item"><div class="item__name">Garden Plate</div><div class="item__desc">picante bread, chilli, olives</div></div>
    <div class="item"><div class="item__name">Picante Plate</div><div class="item__desc">picante bread, chilli, meat &amp; armadillo</div></div>
    <div class="item"><div class="item__name">Sea Plate</div><div class="item__desc">picante bread, chilli, meat &amp; armadillo</div></div>
    <div class="item"><div class="item__name">Picante Plate, Funghi e Prosciutto</div><div class="item__desc">picante bread, chilli, meat &amp; armadillo</div></div>
  </div>
  <div class="rule"></div>
  <section class="mains">
    <h2 class="section-title">Main Courses</h2>
    <div class="mains__list">
      <div class="item"><div class="item__name">Country Style Spreads</div><div class="item__desc">walnuts, cheese, walnuts, cheese, walnuts, cheese, w/ walnuts, cheese &amp; walnuts, cheese</div></div>
      <div class="item"><div class="item__name">Country Style Spreads</div><div class="item__desc">walnuts, cheese, walnuts, cheese, walnuts, cheese, w/ walnuts, cheese &amp; walnuts, cheese</div></div>
      <div class="item"><div class="item__name">Traditional Style Soups for Vegetarians</div><div class="item__desc">walnuts, cheese, walnuts, cheese, walnuts, cheese, w/ walnuts, cheese &amp; walnuts, cheese</div></div>
      <div class="item"><div class="item__name">Country Spreads</div><div class="item__desc">walnuts, cheese, walnuts, cheese, walnuts, cheese, w/ walnuts, cheese &amp; walnuts, cheese</div></div>
    </div>
  </section>
</article>

<aside class="card">
  <div class="card__binding">
    <span class="card__ring"></span><span class="card__ring"></span><span class="card__ring"></span><span class="card__ring"></span>
  </div>
  <div class="card__body">
    <div class="card__photo" role="img" aria-label="Photo of a grilled crostini topped with chopped tomatoes and basil"></div>
    <h2 class="card__title">Amazing Crostini</h2>
    <p class="card__text">The toppings can be as simple or as luxurious as you like, from chopped herbs to lovely flaked fish.</p>
  </div>
</aside>

</body>
</html>
```